Socialbook Cover & Profile Branding for OlvendrA Technologies

We need a modern, premium Socialbook cover image for our company Olvendra Technologies GmbH. The design should be clean, professional, and aligned with our corporate colors (neon green and deep blue) as well as our logo. It should clearly represent us as a technology and IT consulting company with a strong focus on software testing and quality assurance.

Since Olvendra Technologies is also active in the U.S. market, the design may include global or U.S.-related elements (e.g., subtle references to international presence, tech innovation with a global reach).

Requirements:

Integration of the Olvendra logo and brand colors

Modern, premium look with a tech-driven feel

Clear, simple layout that looks good on desktop and mobile

Optional: subtle U.S./international references to highlight our global presence

Goal:
A professional, eye-catching Socialbook cover image that strengthens our brand identity and reflects our international expansion into the U.S. market.

Target Market(s)

Medium to large enterprises in the technology, finance, and energy sectors - Companies looking for premium IT consulting, software testing, and quality assurance services - Decision makers and executives (CIOs, CTOs, IT managers) in Europe and the United States - A global audience that values innovation, professionalism, and trust

Industry/Entity Type

Information Technology & Consulting Software Testing & Quality Assurance Technology / Professional Services Global IT Consulting with U.S. Market Presence

Requirements
Must have
• Integration of the Olvendra Technologies logo and brand colors (Neon Green & Deep Blue) Modern, premium design with a strong tech-oriented look and feel Clean and professional layout, optimized for both desktop and mobile display Clear visibility of the brand identity (technology, IT consulting, software testing, quality assurance) Subtle reference to U.S. presence / global expansion (to highlight activity in both Germany and the U.S.) Balanced use of colors and space for a high-end, corporate appearance
Nice to have
• Subtle animations or motion effects (e.g., light gradients, moving lines, glowing accents) Dark/Light version option for different moods or seasonal campaigns Integration of social media icons (LinkedIn, Instagram, Socialbook) in a clean, minimal way Tech-inspired background elements (digital patterns, abstract shapes, network grids) Space for an optional tagline or slogan (e.g., “Innovation. Quality. Global Impact.”) Adaptability for other platforms (so the design style can be reused for LinkedIn or Twitter headers)
Should not have
• Cluttered or overloaded layouts that reduce clarity Low-quality stock photos or generic imagery that doesn’t fit a premium brand Use of colors outside the Olvendra brand identity (Neon Green & Deep Blue) Outdated design styles (e.g., heavy gradients, 3D effects, drop shadows) Complex text blocks that make the design look busy Elements that distract from the logo and core brand message Pop-art or playful styles that don’t match the premium, professional tech look

```html
<!DOCTYPE html>
<html lang="en">
<head>
<meta charset="utf-8">
<title>Olvendra Technologies GmbH – Social Cover</title>
<link href="https://fonts.googleapis.com/css2?family=Open+Sans:wght@400;600;700&display=swap" rel="stylesheet">
<style>
  :root {
    --stage: #979aa3;
    --cover-deep: #050505;
    --cover-mid: #1c1c1c;
    --ink-light: #ffffff;
    --brand-green: #6cc02e;
    --brand-teal: #1aa79a;
    --brand-blue: #2f5fb0;
    --ui-blue: #1877f2;
    --ui-ink: #050505;
    --ui-muted: #65676b;
    --ui-chip: #e4e6eb;
    --ui-bg: #f0f2f5;
    --ui-line: #ced0d4;
  }
  html, body {
    margin: 0;
    width: 1200px;
    height: 1200px;
    overflow: hidden;
    background: var(--stage);
    font-family: "Open Sans", Arial, sans-serif;
  }
  .canvas { position: relative; width: 1200px; height: 1200px; }

  /* ---------- Cover artwork ---------- */
  .cover {
    position: absolute;
    width: 1010px;
    height: 380px;
    overflow: hidden;
    background: var(--cover-deep);
    color: var(--ink-light);
  }
  .cover--flat { left: 93px; top: 663px; }
  .cover--page { left: 179px; top: 30px; transform: scale(0.6604); transform-origin: 0 0; }
  .cover__texture {
    position: absolute;
    inset: 0;
    background:
      radial-gradient(ellipse at 35% 30%, var(--cover-mid) 0%, transparent 60%),
      radial-gradient(ellipse at 80% 80%, #161616 0%, transparent 55%),
      linear-gradient(135deg, #0d0d0d 0%, #202020 45%, #000 100%);
  }
  .brand-dot {
    position: absolute;
    left: 113px;
    top: 70px;
    width: 190px;
    height: 190px;
    border-radius: 50%;
    background: var(--brand-teal);
  }
  .brand-block {
    position: absolute;
    left: 350px;
    top: 72px;
    width: 590px;
    text-align: center;
  }
  .brand-name { margin: 0; font-weight: 600; line-height: 1; }
  .brand-name__main { display: block; font-size: 106px; letter-spacing: 1px; text-transform: uppercase; }
  .brand-name__sub { display: block; margin-top: 3px; font-size: 58px; }
  .brand-rule {
    width: 552px;
    height: 2px;
    margin: 24px auto 0;
    background: linear-gradient(90deg, var(--brand-green), var(--brand-teal), var(--brand-blue));
  }
  .tagline { margin: 9px 0 0; font-size: 28px; line-height: 1; white-space: nowrap; }

  /* ---------- Page preview ---------- */
  .page {
    position: absolute;
    left: 88px;
    top: 124px;
    width: 1024px;
    height: 502px;
    overflow: hidden;
    background: var(--ui-bg);
    color: var(--ui-ink);
  }
  .page__head {
    position: absolute;
    left: 0; top: 0;
    width: 1024px; height: 374px;
    background: linear-gradient(180deg, #c9cacd 0%, #e4e5e8 40%, #ffffff 60%);
    border-bottom: 1px solid var(--ui-line);
  }
  .page__headband { position: absolute; left: 179px; top: 30px; width: 667px; height: 344px; background: #fff; }
  .topbar {
    position: absolute; left: 0; top: 0;
    width: 1024px; height: 29px;
    background: #fff;
    border-bottom: 1px solid #dadde1;
    z-index: 3;
  }
  .topbar__mark { position: absolute; left: 9px; top: 4px; width: 21px; height: 21px; border-radius: 50%; background: var(--ui-blue); }
  .topbar__search {
    position: absolute; left: 35px; top: 4px; width: 148px; height: 20px;
    border-radius: 10px; background: var(--ui-bg);
    font-size: 8px; line-height: 20px; color: var(--ui-muted); padding-left: 18px; box-sizing: border-box;
  }
  .topbar__search svg { position: absolute; left: 6px; top: 6px; }
  .topbar__tab { position: absolute; top: 7px; width: 16px; height: 16px; }
  .badge {
    position: absolute; left: 519px; top: 3px;
    background: #e41e3f; color: #fff; font-size: 6px; font-weight: 700;
    border-radius: 5px; padding: 0 3px; line-height: 9px;
  }
  .topbar__round { position: absolute; top: 4px; width: 21px; height: 21px; border-radius: 50%; background: var(--ui-chip); }
  .topbar__round svg { position: absolute; left: 5px; top: 5px; }
  .topbar__avatar { background: #000; }

  .profile {
    position: absolute; left: 199px; top: 241px;
    width: 90px; height: 90px; border-radius: 50%;
    background: #fff; border: 2px solid var(--ui-blue); box-sizing: border-box;
    z-index: 2;
  }
  .profile__inner {
    position: absolute; inset: 3px; border-radius: 50%;
    background: radial-gradient(circle at 40% 35%, #262626, #000 70%);
    color: #fff; text-align: center;
  }
  .profile__dot { position: absolute; left: 8px; top: 37px; width: 10px; height: 10px; border-radius: 50%; background: var(--brand-teal); }
  .profile__name { position: absolute; left: 20px; top: 34px; font-size: 7.5px; font-weight: 600; line-height: 1; }
  .profile__sub { position: absolute; left: 20px; top: 43px; font-size: 4.5px; font-weight: 600; line-height: 1; }

  .page-title { position: absolute; left: 296px; top: 281px; margin: 0; font-size: 16px; font-weight: 600; line-height: 1.2; }
  .page-slogan { position: absolute; left: 296px; top: 303px; margin: 0; font-size: 10.5px; font-weight: 600; line-height: 1.2; }
  .page-stats { position: absolute; left: 296px; top: 323px; margin: 0; font-size: 9px; line-height: 1.2; color: var(--ui-muted); }

  .btn {
    position: absolute; top: 306px; height: 18px;
    border-radius: 4px; background: var(--ui-chip);
    font-size: 7.5px; font-weight: 600; line-height: 18px; text-align: center;
    display: flex; align-items: center; justify-content: center; gap: 3px;
  }
  .btn--follow { left: 650px; width: 60px; }
  .btn--message { left: 715px; width: 58px; background: var(--ui-blue); color: #fff; }
  .btn--search { left: 777px; width: 51px; }
  .btn__round { width: 7px; height: 7px; border-radius: 50%; background: #fff; }

  .page-rule { position: absolute; left: 196px; top: 342px; width: 632px; height: 1px; background: var(--ui-line); }
  .tabs { position: absolute; left: 0; top: 353px; font-size: 7.5px; font-weight: 600; color: var(--ui-muted); }
  .tabs span { position: absolute; white-space: nowrap; line-height: 10px; }
  .tabs .is-active { color: var(--ui-blue); }
  .tabs__line { position: absolute; left: 196px; top: 370px; width: 38px; height: 2px; background: var(--ui-blue); }
  .tabs__more { position: absolute; left: 803px; top: 349px; width: 25px; height: 19px; border-radius: 4px; background: var(--ui-chip); font-size: 9px; font-weight: 700; text-align: center; line-height: 14px; }

  .card { position: absolute; background: #fff; border-radius: 5px; }
  .card--intro { left: 196px; top: 383px; width: 260px; height: 140px; }
  .card--postshead { left: 465px; top: 383px; width: 363px; height: 27px; }
  .card--post { left: 465px; top: 419px; width: 363px; height: 110px; }
  .card__title { position: absolute; left: 8px; margin: 0; font-size: 12px; font-weight: 600; line-height: 1.2; }
  .intro__text { position: absolute; left: 0; top: 26px; width: 260px; text-align: center; font-size: 8px; margin: 0; }
  .intro__rule { position: absolute; left: 8px; top: 44px; width: 245px; height: 1px; background: var(--ui-line); }
  .intro__row { position: absolute; left: 8px; display: flex; align-items: center; gap: 6px; font-size: 8px; }
  .intro__row b { font-weight: 700; }
  .intro__link { color: var(--ui-blue); }
  .filters {
    position: absolute; left: 306px; top: 4px; width: 48px; height: 19px;
    border-radius: 4px; background: var(--ui-bg); font-size: 7.5px; font-weight: 600;
    display: flex; align-items: center; justify-content: center; gap: 3px;
  }
  .post__avatar { position: absolute; left: 7px; top: 4px; width: 24px; height: 24px; border-radius: 50%; background: #000; }
  .post__avatar::after { content: ""; position: absolute; left: 4px; top: 10px; width: 4px; height: 4px; border-radius: 50%; background: var(--brand-teal); }
  .post__name { position: absolute; left: 36px; top: 5px; margin: 0; font-size: 9.5px; font-weight: 600; line-height: 1.2; }
  .post__date { position: absolute; left: 35px; top: 18px; margin: 0; font-size: 7px; color: var(--ui-muted); line-height: 1.2; }
  .post__menu { position: absolute; left: 341px; top: 7px; font-size: 9px; font-weight: 700; color: var(--ui-muted); }
  .post__body { position: absolute; left: 9px; top: 32px; width: 346px; margin: 0; font-size: 7.6px; line-height: 11px; }
  .post__tag { color: var(--ui-blue); }
</style>
</head>
<body>
  <div class="canvas">

    <section class="page" aria-label="Social page preview">
      <div class="page__head"></div>
      <div class="page__headband"></div>

      <header class="topbar">
        <span class="topbar__mark"></span>
        <div class="topbar__search">
          <svg width="8" height="8" viewBox="0 0 10 10"><circle cx="4" cy="4" r="3" fill="none" stroke="#65676b" stroke-width="1.3"/><path d="M6.3 6.3 9 9" stroke="#65676b" stroke-width="1.3"/></svg>
          Search Socialbook
        </div>
        <svg class="topbar__tab" style="left:358px" viewBox="0 0 16 16"><path d="M2 8 8 2l6 6v6H10v-4H6v4H2z" fill="none" stroke="#65676b" stroke-width="1.2"/></svg>
        <svg class="topbar__tab" style="left:431px" viewBox="0 0 16 16"><circle cx="6" cy="5" r="2.5" fill="none" stroke="#65676b" stroke-width="1.2"/><circle cx="11" cy="5" r="2" fill="none" stroke="#65676b" stroke-width="1.2"/><path d="M1.5 14c0-3 2-5 4.5-5s4.5 2 4.5 5M11 9c2 0 3.5 1.5 3.5 4" fill="none" stroke="#65676b" stroke-width="1.2"/></svg>
        <svg class="topbar__tab" style="left:504px" viewBox="0 0 16 16"><rect x="2" y="3" width="12" height="9" rx="1.5" fill="none" stroke="#65676b" stroke-width="1.2"/><path d="M7 5.5v4l3-2z" fill="#65676b"/><path d="M5 14h6" stroke="#65676b" stroke-width="1.2"/></svg>
        <span class="badge">9+</span>
        <svg class="topbar__tab" style="left:577px" viewBox="0 0 16 16"><path d="M2 6 3.5 2h9L14 6M2 6h12M3 6v8h10V6M6.5 14v-4h3v4" fill="none" stroke="#65676b" stroke-width="1.2"/></svg>
        <svg class="topbar__tab" style="left:651px" viewBox="0 0 16 16"><rect x="2.5" y="2.5" width="11" height="11" rx="1" fill="none" stroke="#65676b" stroke-width="1.2"/><path d="M5 13.5V6.5h6" fill="none" stroke="#65676b" stroke-width="1.2"/></svg>
        <span class="topbar__round" style="left:917px"><svg width="11" height="11" viewBox="0 0 11 11" fill="#050505"><circle cx="2" cy="2" r="1.2"/><circle cx="5.5" cy="2" r="1.2"/><circle cx="9" cy="2" r="1.2"/><circle cx="2" cy="5.5" r="1.2"/><circle cx="5.5" cy="5.5" r="1.2"/><circle cx="9" cy="5.5" r="1.2"/><circle cx="2" cy="9" r="1.2"/><circle cx="5.5" cy="9" r="1.2"/><circle cx="9" cy="9" r="1.2"/></svg></span>
        <span class="topbar__round" style="left:943px"><svg width="11" height="11" viewBox="0 0 11 11"><circle cx="5.5" cy="5.5" r="4.5" fill="#050505"/></svg></span>
        <span class="topbar__round" style="left:968px"><svg width="11" height="11" viewBox="0 0 11 11"><path d="M5.5 1C3.5 1 2.5 2.6 2.5 4.5V7L1.5 8.5h8L8.5 7V4.5C8.5 2.6 7.5 1 5.5 1zM4.3 9.5a1.2 1.2 0 0 0 2.4 0z" fill="#050505"/></svg></span>
        <span class="topbar__round topbar__avatar" style="left:993px"></span>
      </header>

      <div class="cover cover--page">
        <div class="cover__texture" role="img" aria-label="Dark faceted low-poly background in black and charcoal tones"></div>
        <div class="brand-dot"></div>
        <div class="brand-block">
          <h2 class="brand-name">
            <span class="brand-name__main">Olvendra</span>
            <span class="brand-name__sub">Technologies GmbH</span>
          </h2>
          <div class="brand-rule"></div>
          <p class="tagline">Empowering Technology. Enabling Success.</p>
        </div>
      </div>

      <div class="profile">
        <div class="profile__inner">
          <span class="profile__dot"></span>
          <span class="profile__name">OLVENDRA</span>
          <span class="profile__sub">Technologies GmbH</span>
        </div>
      </div>

      <h1 class="page-title">Olvendra Technologies Gmbh</h1>
      <p class="page-slogan">Empowering Technology. Enabling Success.</p>
      <p class="page-stats">7.7M followers . 70 following</p>

      <div class="btn btn--follow">
        <svg width="8" height="8" viewBox="0 0 8 8"><rect x="0.5" y="1" width="7" height="6.5" rx="1" fill="#050505"/><path d="M2 4.3 3.4 5.6 6 2.8" fill="none" stroke="#fff" stroke-width="1"/></svg>Following
      </div>
      <div class="btn btn--message"><span class="btn__round"></span>Message</div>
      <div class="btn btn--search">
        <svg width="8" height="8" viewBox="0 0 10 10"><circle cx="4" cy="4" r="3" fill="none" stroke="#050505" stroke-width="1.4"/><path d="M6.3 6.3 9 9" stroke="#050505" stroke-width="1.4"/></svg>Search
      </div>

      <div class="page-rule"></div>
      <nav class="tabs">
        <span class="is-active" style="left:204px">Posts</span>
        <span style="left:243px">About</span>
        <span style="left:283px">Mentions</span>
        <span style="left:334px">Reviews</span>
        <span style="left:383px">Followers</span>
        <span style="left:435px">Photos</span>
        <span style="left:479px">More ▾</span>
      </nav>
      <div class="tabs__line"></div>
      <div class="tabs__more">...</div>

      <article class="card card--intro">
        <h3 class="card__title" style="top:6px">Intro</h3>
        <p class="intro__text">The ONLY official page managed by Lemon Press.</p>
        <div class="intro__rule"></div>
        <div class="intro__row" style="top:56px">
          <svg width="10" height="10" viewBox="0 0 10 10"><circle cx="5" cy="5" r="5" fill="#8a8d91"/><path d="M5 4.3v3.2" stroke="#fff" stroke-width="1.2"/><circle cx="5" cy="2.8" r=".7" fill="#fff"/></svg>
          <span><b>Page</b> . Art</span>
        </div>
        <div class="intro__row" style="top:78px">
          <svg width="10" height="10" viewBox="0 0 10 10" fill="none" stroke="#8a8d91" stroke-width=".9"><circle cx="5" cy="5" r="4.4"/><ellipse cx="5" cy="5" rx="2" ry="4.4"/><path d="M.6 5h8.8M1.5 2.8h7M1.5 7.2h7"/></svg>
          <span class="intro__link">olvendra.example/page</span>
        </div>
        <div class="intro__row" style="top:100px">
          <svg width="10" height="10" viewBox="0 0 10 10"><path d="M5 .5 6.4 3.5 9.6 3.8 7.2 6 7.9 9.3 5 7.6 2.1 9.3 2.8 6 .4 3.8 3.6 3.5z" fill="#8a8d91"/></svg>
          <span>Rating . 5.0 (4,701)</span>
        </div>
      </article>

      <div class="card card--postshead">
        <h3 class="card__title" style="top:6px">Posts</h3>
        <div class="filters">
          <svg width="8" height="7" viewBox="0 0 8 7" stroke="#050505" stroke-width=".8" fill="none"><path d="M0 1.5h8M0 5.5h8"/><circle cx="2.5" cy="1.5" r="1" fill="#fff"/><circle cx="5.5" cy="5.5" r="1" fill="#fff"/></svg>Filters
        </div>
      </div>

      <article class="card card--post">
        <span class="post__avatar"></span>
        <p class="post__name">Olvendra Technologies Gmbh</p>
        <p class="post__date">18 January 2022 · ◍</p>
        <span class="post__menu">···</span>
        <p class="post__body">Lorem ipsum dolor sit amet, consectetur adipiscing elit, sed do eiusmod tempor incididunt ut labore et dolore magna aliqua. Quis ipsum suspendisse ultrices gravida. Risus commodo viverra maecenas accumsan lacus vel facilisis. <span class="post__tag">#food</span></p>
      </article>
    </section>

    <section class="cover cover--flat">
      <div class="cover__texture" role="img" aria-label="Dark faceted low-poly background in black and charcoal tones"></div>
      <div class="brand-dot"></div>
      <div class="brand-block">
        <h2 class="brand-name">
          <span class="brand-name__main">Olvendra</span>
          <span class="brand-name__sub">Technologies GmbH</span>
        </h2>
        <div class="brand-rule"></div>
        <p class="tagline">Empowering Technology. Enabling Success.</p>
      </div>
    </section>

  </div>
</body>
</html>
```